Lawyers in the Netherlands website + logo

We are going in 2015 to launch a website where all law firms in the Netherlands and have the opportunity to place an ad program.

The domain name wil be:

kantoorvinder.website

We want a responsive PSD bootstrap twitter 1170 pixel grid.
for the homepage, result page and the detail page of the customer.

This sites we like:
https://www.qorvantis.com/lawyers

https://lawyers.qorvantis.com/lawyer/tim-garsby-7305826

http://solicitordirectory.brevimark.co.uk/
Map of the Netherlands?

http://solicitordirectory.brevimark.co.uk/listing/category-search/commercial
http://www.tandelvo.com.au/find-a-lawyer/banking-finance-law/

```html
<!DOCTYPE html>
<html lang="en">
<head>
<meta charset="utf-8">
<title>KantoorVinder – Find a Lawyer</title>
<link rel="stylesheet" href="https://fonts.googleapis.com/css2?family=Roboto:wght@300;400;500;700;900&display=swap">
<style>
:root{
  --blue:#1e7fd8;
  --blue-dark:#1565c0;
  --ink:#222831;
  --text:#666b73;
  --muted:#8a9099;
  --line:#dcdfe3;
  --page:#f1f2f4;
  --white:#ffffff;
  --dark-band:#1b1e24;
  --footer:#111826;
  --footer-text:#8d96a6;
}
*{box-sizing:border-box;margin:0;padding:0}
html,body{width:1200px;height:2571px;overflow:hidden}
body{font-family:"Roboto",Arial,sans-serif;background:var(--page);color:var(--text);position:relative}
a{color:inherit;text-decoration:none}
.abs{position:absolute}

/* header */
.site-header{position:absolute;left:0;top:0;width:1200px;height:105px;background:var(--white)}
.brand{position:absolute;left:90px;top:22px;display:flex;align-items:center;gap:10px}
.brand-mark{width:34px;height:34px;background:var(--ink)}
.brand-name{font-size:26px;font-weight:500;color:var(--ink);letter-spacing:-.3px}
.top-actions{position:absolute;left:428px;top:30px;display:flex;gap:10px;align-items:center}
.btn{background:var(--blue);color:var(--white);font-size:12px;padding:7px 18px;border-radius:2px}
.phone{position:absolute;left:722px;top:33px;font-size:18px;color:var(--ink);display:flex;gap:7px;align-items:center}
.page-tabs{position:absolute;left:892px;top:36px;display:flex;gap:26px;font-size:12px;color:var(--ink)}
.page-tabs .active{color:var(--blue);border-bottom:2px solid var(--blue);padding-bottom:4px}
.main-nav{position:absolute;left:425px;top:78px;display:flex;gap:30px;font-size:12.5px;color:var(--ink)}
.social{display:flex;gap:7px}
.social span{width:20px;height:20px;border-radius:50%;background:var(--ink);display:block}
.header-social{position:absolute;left:985px;top:74px}

/* hero */
.hero{position:absolute;left:85px;top:105px;width:1030px;height:447px;background:linear-gradient(160deg,#9aa0a6 0%,#5d636b 45%,#2f343a 100%)}
.hero-photo{position:absolute;inset:0}
.hero h1{position:absolute;left:0;right:0;top:138px;text-align:center;color:var(--white);font-size:52px;font-weight:900;line-height:62px;text-shadow:0 2px 6px rgba(0,0,0,.55);letter-spacing:-.5px}
.search{position:absolute;left:92px;top:318px;display:flex;gap:10px}
.search .field{width:408px;height:50px;background:var(--white);font-size:14px;color:var(--muted);padding:16px 16px}
.search .field.loc{width:358px}
.search .go{width:50px;height:50px;background:var(--blue);display:flex;align-items:center;justify-content:center}

/* features */
.features{position:absolute;left:100px;top:605px;width:1010px;display:grid;grid-template-columns:repeat(3,1fr);column-gap:40px;row-gap:34px}
.feature h3{font-size:16px;font-weight:500;color:var(--ink);display:flex;align-items:center;gap:10px;margin-bottom:8px}
.feature p{font-size:12px;line-height:16px;color:var(--muted);width:270px}
.divider{position:absolute;left:100px;top:866px;width:1000px;height:1px;background:var(--line)}

/* directory lists */
.directory{position:absolute;top:905px}
.directory h2{font-size:17px;font-weight:400;color:var(--blue);margin-bottom:14px}
.directory h2 b{font-weight:400;color:var(--ink)}
.dir-cols{display:flex}
.dir-cols ul{list-style:none;font-size:12px;line-height:20px;color:var(--text)}
.dir-cols ul li:first-child{color:var(--blue)}

/* happy clients */
.clients{position:absolute;left:85px;top:1166px;width:1030px;height:400px;background:radial-gradient(ellipse at 50% 55%,#3a3f47 0%,#1c1f25 60%,#121418 100%)}
.clients h2{position:absolute;top:48px;left:0;right:0;text-align:center;color:var(--white);font-size:20px;font-weight:500;letter-spacing:.5px}
.quote{position:absolute;top:100px;width:282px;height:145px;border:1px solid rgba(255,255,255,.8);padding:14px 14px 0 52px;color:#e4e6ea;font-size:12.5px;line-height:17px}
.quote .q{position:absolute;left:14px;top:14px;width:24px;height:24px;border:1px solid #e4e6ea;border-radius:50%;display:flex;align-items:center;justify-content:center;font-size:16px;line-height:1}
.quote:after{content:"";position:absolute;left:38px;bottom:-11px;width:20px;height:20px;background:#22252b;border-right:1px solid rgba(255,255,255,.8);border-bottom:1px solid rgba(255,255,255,.8);transform:rotate(45deg)}
.client{position:absolute;top:268px;display:flex;align-items:center;gap:12px;color:var(--white)}
.avatar{width:56px;height:56px;border-radius:50%;background:linear-gradient(135deg,#b48a6a,#5a3d2c)}
.client small{display:block;font-size:11px;color:#c9cdd3}
.client span{font-size:17px}

/* about */
.about-title{font-size:16px;font-weight:500;color:var(--blue)}
.about-photo{position:absolute;left:100px;top:1650px;width:330px;height:190px;background:linear-gradient(135deg,#6d6f72,#2a2b2d 60%,#8a6f52);box-shadow:0 0 0 4px var(--white)}
.about-text{position:absolute;left:452px;top:1648px;width:262px;font-size:12px;line-height:17px;color:var(--muted)}
.accordion-bar{position:absolute;left:745px;width:355px;height:36px;background:var(--white);border:1px solid var(--line);font-size:12px;color:var(--text);padding:10px 12px}
.accordion-bar i{position:absolute;right:8px;top:8px;width:18px;height:18px;border:1px solid var(--muted);border-radius:50%}
.accordion-text{position:absolute;left:745px;width:355px;font-size:12px;line-height:17px;color:var(--muted)}

/* press */
.press{position:absolute;left:85px;top:1897px;width:1030px;height:130px;background:var(--white);border:1px solid var(--line);display:flex;justify-content:space-around;align-items:center;padding:0 40px}
.press span{display:block;height:30px;background:#b3b6bb}

/* footer */
.site-footer{position:absolute;left:0;top:2071px;width:1200px;height:500px;background:var(--footer);color:var(--footer-text)}
.f-col{position:absolute;top:56px}
.f-col h4{font-size:16px;font-weight:400;color:var(--white);margin-bottom:18px}
.f-col ul{list-style:none;font-size:12px;line-height:19px}
.post{display:flex;gap:10px;margin-bottom:20px}
.post .thumb{width:54px;height:54px;background:linear-gradient(135deg,#8a6a52,#3a2a22);border:2px solid #e5e5e5;flex:none}
.post p{font-size:12px;line-height:15px;width:200px}
.post .date{color:var(--white);font-size:12px;margin-top:3px}
.contact p{font-size:12px;line-height:18px;margin-bottom:18px;width:240px}
.f-bottom{position:absolute;left:85px;top:395px;font-size:12px;line-height:18px}
.f-social{position:absolute;left:605px;top:400px;transform:translateX(-50%)}
.f-social span{width:26px;height:26px;background:#3b4354}
.f-brand{position:absolute;right:90px;top:402px;display:flex;align-items:center;gap:10px}
.f-brand .brand-mark{background:var(--white);width:30px;height:30px}
.f-brand .brand-name{color:var(--white);font-size:22px}
</style>
</head>
<body>

<header class="site-header">
  <div class="brand"><span class="brand-mark"></span><span class="brand-name">KantoorVinder</span></div>
  <div class="top-actions"><a class="btn">Sign in</a><a class="btn">Lawyers Get Listed</a></div>
  <div class="phone">
    <svg width="16" height="16" viewBox="0 0 24 24"><path fill="#222831" d="M6.6 10.8a15 15 0 0 0 6.6 6.6l2.2-2.2c.3-.3.7-.4 1-.2 1.1.4 2.3.6 3.6.6.6 0 1 .4 1 1V20c0 .6-.4 1-1 1A17 17 0 0 1 3 4c0-.6.4-1 1-1h3.5c.6 0 1 .4 1 1 0 1.3.2 2.5.6 3.6.1.3 0 .7-.2 1z"/></svg>
    123.456.7890
  </div>
  <nav class="page-tabs"><a class="active">Home Page</a><a>Result Page</a><a>Detail Page</a></nav>
  <nav class="main-nav"><a>Find a Lawyer</a><a>Legal Answers</a><a>Law</a><a>More</a><a>Lawyers Get Listed</a><a>FAQ</a></nav>
  <div class="social header-social"><span></span><span></span><span></span><span></span></div>
</header>

<section class="hero">
  <div class="hero-photo" role="img" aria-label="Photo of lawyers meeting in an office"></div>
  <h1>Helping You With Your<br>Legal Needs</h1>
  <div class="search">
    <div class="field">Search Legal Issue or Lawyer Name</div>
    <div class="field loc">City, State or Zip Code</div>
    <div class="go"><svg width="18" height="18" viewBox="0 0 24 24"><circle cx="10" cy="10" r="6.5" fill="none" stroke="#fff" stroke-width="2.5"/><path d="M15 15l6 6" stroke="#fff" stroke-width="2.5"/></svg></div>
  </div>
</section>

<section class="features">
  <div class="feature"><h3><svg width="18" height="16" viewBox="0 0 18 16"><rect x="1" y="4" width="16" height="11" fill="#222831"/><rect x="6" y="1" width="6" height="4" fill="none" stroke="#222831" stroke-width="2"/></svg>Experience Law Firm</h3><p>Lorem ipsum dolor sit amet, consectetuer adipiscing elit, sed diam nonummy nibh euismod tincidunt ut laoreet.</p></div>
  <div class="feature"><h3><svg width="18" height="16" viewBox="0 0 18 16"><path d="M4 1h10v4a5 5 0 0 1-10 0z" fill="#222831"/><rect x="8" y="9" width="2" height="4" fill="#222831"/><rect x="5" y="13" width="8" height="2" fill="#222831"/></svg>Compassionate Law Firm</h3><p>Lorem ipsum dolor sit amet, consectetuer adipiscing elit, sed diam nonummy nibh euismod tincidunt ut laoreet.</p></div>
  <div class="feature"><h3><svg width="18" height="16" viewBox="0 0 18 16"><path d="M2 1h14v14l-7-4-7 4z" fill="#222831"/></svg>Redding Law Firm</h3><p>Lorem ipsum dolor sit amet, consectetuer adipiscing elit, sed diam nonummy nibh euismod tincidunt ut laoreet.</p></div>
  <div class="feature"><h3><svg width="18" height="16" viewBox="0 0 18 16"><path d="M9 1v14M3 4h12M3 4l-2 6h4zM15 4l-2 6h4z" stroke="#222831" stroke-width="1.5" fill="#222831"/></svg>Our Philosophy</h3><p>Lorem ipsum dolor sit amet, consectetuer adipiscing elit, sed diam nonummy nibh euismod tincidunt ut laoreet.</p></div>
  <div class="feature"><h3><svg width="18" height="16" viewBox="0 0 18 16"><rect x="6" y="1" width="8" height="5" transform="rotate(40 10 4)" fill="#222831"/><path d="M7 8l-5 6" stroke="#222831" stroke-width="2.5"/><rect x="9" y="13" width="8" height="2" fill="#222831"/></svg>Efficiency</h3><p>Lorem ipsum dolor sit amet, consectetuer adipiscing elit, sed diam nonummy nibh euismod tincidunt ut laoreet.</p></div>
  <div class="feature"><h3><svg width="18" height="16" viewBox="0 0 18 16"><path d="M1 5L9 1l8 4z" fill="#222831"/><rect x="3" y="6" width="2" height="7" fill="#222831"/><rect x="8" y="6" width="2" height="7" fill="#222831"/><rect x="13" y="6" width="2" height="7" fill="#222831"/><rect x="1" y="13" width="16" height="2" fill="#222831"/></svg>Value for money</h3><p>Lorem ipsum dolor sit amet, consectetuer adipiscing elit, sed diam nonummy nibh euismod tincidunt ut laoreet.</p></div>
</section>

<div class="divider"></div>

<section class="directory" style="left:100px">
  <h2>Practice Area/<b>Find Lawyers by</b></h2>
  <div class="dir-cols" style="gap:0">
    <ul style="width:125px"><li>Bankruptcy</li><li>Business Law</li><li>Consumer Law</li><li>Criminal Law</li><li>Divorce</li><li>DUI &amp; DWI</li><li>Employment Law</li></ul>
    <ul style="width:215px"><li>Estate Planning</li><li>Family Law</li><li>Foreclosure Defense</li><li>Immigration Law</li><li>Intellectual Property</li><li>Medical Malpractice</li><li>Nursing Home Abuse &amp; Neglect</li></ul>
    <ul style="width:150px"><li>Personal Injury</li><li>Probate</li><li>Products Liability</li><li>Real Estate Law</li><li>Tax Law</li><li>Traffic Tickets</li><li>Workers' Compensation</li></ul>
  </div>
</section>
<section class="directory" style="left:640px">
  <h2>State/<b>Find Lawyers by</b></h2>
  <div class="dir-cols">
    <ul style="width:115px"><li>Alabama</li><li>Alaska</li><li>Arizona</li><li>Arkansas</li><li>California</li><li>Colorado</li><li>Connecticut</li></ul>
    <ul style="width:115px"><li>Delaware</li><li>Florida</li><li>Georgia</li><li>Hawaii</li><li>Idaho</li><li>Illinois</li><li>Indiana</li></ul>
    <ul style="width:115px"><li>Louisiana</li><li>Maine</li><li>Maryland</li><li>Massachusetts</li><li>Michigan</li><li>Minnesota</li><li>Mississippi</li></ul>
    <ul style="width:115px"><li>Missouri</li><li>Montana</li><li>Nebraska</li><li>Nevada</li><li>New Hampshire</li><li>New Jersey</li><li>New Mexico</li></ul>
  </div>
</section>

<section class="clients" role="img" aria-label="Dark background photo behind client testimonials">
  <h2>HAPPY CLIENTS</h2>
  <div class="quote" style="left:45px"><span class="q">“</span>Lorem ipsum dolor sit amet, consectetuer adipiscing elit, sed diam nonummy nibh euismod tincidunt ut laoreet dolore magna aliquam erat volutpat. Ut wisi enim ad minim veniam, quis nostrud exerci tation.</div>
  <div class="quote" style="left:374px"><span class="q">“</span>Lorem ipsum dolor sit amet, consectetuer adipiscing elit, sed diam nonummy nibh euismod tincidunt ut laoreet dolore magna aliquam erat volutpat. Ut wisi enim ad minim veniam, quis nostrud exerci tation.</div>
  <div class="quote" style="left:703px"><span class="q">“</span>Lorem ipsum dolor sit amet, consectetuer adipiscing elit, sed diam nonummy nibh euismod tincidunt ut laoreet dolore magna aliquam erat volutpat. Ut wisi enim ad minim veniam, quis nostrud exerci tation.</div>
  <div class="client" style="left:45px"><div class="avatar" role="img" aria-label="Client portrait"></div><div><small>Fiona</small><span>Lawyer</span></div></div>
  <div class="client" style="left:374px"><div class="avatar" role="img" aria-label="Client portrait"></div><div><small>Fiona</small><span>Lawyer</span></div></div>
  <div class="client" style="left:703px"><div class="avatar" role="img" aria-label="Client portrait"></div><div><small>Fiona</small><span>Lawyer</span></div></div>
</section>

<h2 class="about-title abs" style="left:100px;top:1612px">What Makes Law Firm Different ?</h2>
<div class="about-photo" role="img" aria-label="Photo of a judge's gavel on a desk"></div>
<p class="about-text">Lorem ipsum dolor sit amet, consectetuer adipiscing elit, sed diam nonummy nibh euismod tincidunt ut laoreet dolore magna aliquam erat volutpat. Ut wisi enim ad minim veniam, quis nostrud exerci tation ullamcorper suscipit lobortis nisl ut aliquip ex ea commodo consequat. Duis autem vel eum iriure dolor in hendrerit in vulputate velit esse.</p>

<h2 class="about-title abs" style="left:745px;top:1612px">Where We Practice ?</h2>
<div class="accordion-bar" style="top:1642px">Lorem ipsum dolor sit amet<i></i></div>
<p class="accordion-text" style="top:1688px">Lorem ipsum dolor sit amet, consectetuer adipiscing elit, sed diam nonummy nibh euismod tincidunt ut laoreet dolore magna aliquam erat volutpat. Ut wisi enim ad minim veniam, quis nostrud exerci tation ullamcorper suscipit lobortis nisl ut aliquip ex ea commodo consequat.</p>
<div class="accordion-bar" style="top:1800px">Lorem ipsum dolor sit amet<i></i></div>

<section class="press" aria-label="As featured in">
  <span style="width:205px"></span><span style="width:95px"></span><span style="width:115px"></span><span style="width:130px;height:44px"></span><span style="width:135px;height:40px"></span>
</section>

<footer class="site-footer">
  <div class="f-col" style="left:85px"><h4>Popular Categories</h4><ul><li>Criminal Law</li><li>Family Law</li><li>Immigration Law</li><li>Insurance Law</li><li>Negligence Claims</li><li>Teacher Law</li><li>Wills, Probate, &amp; Estate Planning</li><li>Work Claims</li></ul></div>
  <div class="f-col" style="left:300px"><h4>Our Services</h4><ul><li>Attorney Niche Designs</li><li>Attorney Profile Photography</li><li>Client Think Montage Videos</li><li>Content Writing</li><li>Mobile Website Design</li><li>Internet Marketing Strategies</li><li>Law Firm Website Design</li><li>Lawyer Marketing</li></ul></div>
  <div class="f-col" style="left:505px"><h4>Latest Blog</h4>
    <div class="post"><div class="thumb" role="img" aria-label="Blog post thumbnail"></div><div><p>Lorem ipsum dolor sit amet, consectetuer adipiscing elit, sed diam...</p><p class="date">28, January 2015</p></div></div>
    <div class="post"><div class="thumb" role="img" aria-label="Blog post thumbnail"></div><div><p>Lorem ipsum dolor sit amet, consectetuer adipiscing elit, sed diam...</p><p class="date">27, January 2015</p></div></div>
    <div class="post"><div class="thumb" role="img" aria-label="Blog post thumbnail"></div><div><p>Lorem ipsum dolor sit amet, consectetuer adipiscing elit, sed diam...</p><p class="date">26, January 2015</p></div></div>
  </div>
  <div class="f-col contact" style="left:825px"><h4>Contact Us</h4>
    <p>Keizersgracht Office, Headquarters<br>214 Havenstraat, Utrecht 3511 AB</p>
    <p>Tel : 123.456.7890</p>
    <p>Fax : 123.456.7890</p>
    <p>Email : info@kantoorvinder.website</p>
  </div>
  <div class="f-bottom">© Copyright 2015 kantoorvinder.website . All Reserved</div>
  <div class="social f-social"><span></span><span></span><span></span><span></span></div>
  <div class="f-brand"><span class="brand-mark"></span><span class="brand-name">KantoorVinder</span></div>
</footer>

</body>
</html>
```